Fennick Executive Search - New Business Card Design Project

We are an executive search firm called Fennick Executive Search based in the UK. We require a custom design for a business card. We're looking to convey a professional service to executives for executive search recruitment services. In terms of colours, we like dark blues and grays (maybe even silver incorporated somewhere if we go for a foiled type of card) but we're open to your artistic flare. See our current logo in attachments. We are totally open on design so long as the design is slick and professional.
Updates

Thanks for all your contributions of various designs. I have to say the quality of work has been amazing which is going to make our job quite difficult in the coming days on making a decision. Thanks to you all that have taken the time to submit designs thus far. We'll keep on reviewing and try to narrow down our selection as soon as possible.

Target Market(s)

Executive Search

Industry/Entity Type

Recruitment

Contact Information for Business Card

Fennick Executive Search,
Discreetly Finding & Placing Board Level Talent
Gordon Pellbury, Managing Director,
07823 906417
0117 486 7132
gordon@fennickexecutive.co.uk
fennickexecutive.co.uk
58 Lindmoor Court, Hatherley Road, Bristol, BS32 9QJ

Font styles to use
Sans Serif
Other font styles liked:
• Roboto (which is used in our logo)

Requirements
Must have
• Our logo (It has a subtle fade on it from #02071d at top to #333649 at bottom)
• The logo can be on one side or both sides
• Must be elegant and professional
• We have 2nd slogan CONSULT | INSPIRE | INNOVATE | DELIVER which can be incorporated into the card
Nice to have
• Use of blues and grey colours
• Compatible with similar styling to our website fennickexecutive.co.uk
Should not have
• Must not be overly brash
• Must not contain cartoon characters

```html
<!DOCTYPE html>
<html lang="en">
<head>
<meta charset="utf-8">
<title>Fennick Executive Search — Business Card</title>
<link href="https://fonts.googleapis.com/css2?family=Roboto:wght@300;400;500;700&display=swap" rel="stylesheet">
<style>
  :root {
    --page: #eceae6;
    --card-top: #0d1226;
    --card-bottom: #353849;
    --ink: #ffffff;
    --ink-soft: #d9dbe4;
    --accent: #5566c4;
    --card-w: 580px;
    --card-h: 331px;
  }
  * { box-sizing: border-box; margin: 0; padding: 0; }
  html, body {
    width: 1200px; height: 800px; overflow: hidden;
    background: var(--page);
    font-family: "Roboto", sans-serif;
  }
  .sheet {
    width: 1200px; height: 800px;
    display: flex; flex-direction: column;
    align-items: center; justify-content: center; gap: 40px;
  }
  .card {
    position: relative;
    width: var(--card-w); height: var(--card-h);
    background: linear-gradient(160deg, var(--card-top) 0%, #1c2135 55%, var(--card-bottom) 100%);
    color: var(--ink);
    box-shadow: 0 6px 18px rgba(0,0,0,0.18);
  }
  .brand-name {
    display: block;
    font-weight: 400;
    color: var(--ink);
    line-height: 1;
    text-transform: uppercase;
  }
  .brand-name .line-main { display: block; font-size: 34px; letter-spacing: 1px; }
  .brand-name .line-sub { display: block; font-size: 18px; margin-top: 4px; letter-spacing: 0.5px; }
  .tagline {
    color: var(--accent);
    font-size: 14px; font-weight: 400; line-height: 1.3;
    margin-top: 8px;
  }
  /* back */
  .card-back .brand { position: absolute; left: 34px; bottom: 30px; }
  .card-back .web {
    position: absolute; right: 28px; bottom: 30px;
    display: flex; align-items: center; gap: 8px;
    font-size: 13px; color: var(--ink-soft);
  }
  .card-back .web .icon { stroke: var(--ink); }
  /* front */
  .card-front .brand { position: absolute; left: 30px; top: 108px; width: 230px; }
  .divider {
    position: absolute; left: 270px; top: 60px;
    width: 2px; height: 175px; background: var(--accent);
  }
  .contact { position: absolute; left: 295px; top: 58px; }
  .person-name { font-size: 18px; font-weight: 700; }
  .person-role { font-size: 14px; font-weight: 400; color: var(--ink-soft); margin-top: 4px; }
  .contact-list { list-style: none; margin-top: 26px; }
  .contact-list li {
    display: flex; align-items: center; gap: 12px;
    font-size: 14px; color: var(--ink-soft);
    height: 27px;
  }
  .icon { width: 16px; height: 16px; flex: none; fill: none; stroke: var(--accent); stroke-width: 1.8; stroke-linecap: round; stroke-linejoin: round; }
  .address {
    position: absolute; left: 0; right: 0; bottom: 24px;
    display: flex; justify-content: center; align-items: center; gap: 10px;
    font-size: 14px; color: var(--ink-soft);
  }
</style>
</head>
<body>
<main class="sheet">

  <section class="card card-back" aria-label="Business card back">
    <div class="brand">
      <span class="brand-name"><span class="line-main">Fennick</span><span class="line-sub">Executive Search</span></span>
      <p class="tagline">Discreetly Finding &amp; Placing<br>Board Level Talent</p>
    </div>
    <div class="web">
      <svg class="icon" viewBox="0 0 16 16"><path d="M6.5 9.5l3-3M7 4.5l1.5-1.5a2.5 2.5 0 013.5 3.5L10.5 8M9 11.5L7.5 13A2.5 2.5 0 014 9.5L5.5 8"/></svg>
      <span>fennickexecutive.co.uk</span>
    </div>
  </section>

  <section class="card card-front" aria-label="Business card front">
    <div class="brand">
      <span class="brand-name"><span class="line-main">Fennick</span><span class="line-sub">Executive Search</span></span>
      <p class="tagline">Discreetly Finding &amp; Placing<br>Board Level Talent</p>
    </div>
    <div class="divider"></div>
    <div class="contact">
      <p class="person-name">Gordon Pellbury</p>
      <p class="person-role">Managing Director</p>
      <ul class="contact-list">
        <li><svg class="icon" viewBox="0 0 16 16"><rect x="4" y="1.5" width="8" height="13" rx="1.5"/><path d="M7 12h2"/></svg>07823 906417</li>
        <li><svg class="icon" viewBox="0 0 16 16"><path d="M4.5 6V2h7v4"/><rect x="1.5" y="6" width="13" height="6" rx="1"/><path d="M4.5 10h7v4.5h-7z"/></svg>0117 486 7132</li>
        <li><svg class="icon" viewBox="0 0 16 16"><rect x="1.5" y="3.5" width="13" height="9" rx="1"/><path d="M1.5 4l6.5 5 6.5-5"/></svg>gordon@fennickexecutive.co.uk</li>
        <li><svg class="icon" viewBox="0 0 16 16"><path d="M6.5 9.5l3-3M7 4.5l1.5-1.5a2.5 2.5 0 013.5 3.5L10.5 8M9 11.5L7.5 13A2.5 2.5 0 014 9.5L5.5 8"/></svg>fennickexecutive.co.uk</li>
      </ul>
    </div>
    <p class="address">
      <svg class="icon" viewBox="0 0 16 16"><path d="M8 15s5-5 5-8.5a5 5 0 00-10 0C3 10 8 15 8 15z"/><circle cx="8" cy="6.5" r="1.8"/></svg>
      58 Lindmoor Court, Hatherley Road, Bristol, BS32 9QJ
    </p>
  </section>

</main>
</body>
</html>
```